Easy Business Card / Presentation Cover Design Project

We are looking for a business card design, covers for powerpoint presentations for investors, and possibly simple stationary for a Chicago real estate development firm. Our new logo is attached below.

We rehab and provide newly constructed homes. We are not a real estate brokerage firm (i.e., agents such as Meridale 47) and only operate in the Chicago area.

In terms of design, sophisticated and high end that would appeal to investors (theme should resemble investment banks, hedge funds, private equity rather than tech startup).

Target Market(s)

Investors, banks, financing sources

Industry/Entity Type

Real Estate

Requirements
Must have
• Two deliverables here. 1) Business card 2) Covers for powerpoint presentation.

Must be able to look sophisticated and high end when printed. Please think through the type of printing that will be needed. Would prefer something that can be printed in raised ink but digital is ok as well.

Will be printed on heavy paper.

Business Card: Horizontal Layout, no black backgrounds,

For presentation front cover, should include logo only. For back cover, should include contact info. Horizontal and should not contain any information that will need to be changed (i.e. date or client name)
Nice to have
• Would like to have the edges colored but not required. Please show multiple designs
Should not have
• Should not have any die cut or embossed type of designs. Shape should be standard size.

We are not a design firm, a retail firm, or a consumer product firm.

Please do not incorporate a house, buildings, etc. This must be very professional looking.

```html
<!DOCTYPE html>
<html lang="en">
<head>
<meta charset="utf-8">
<title>Kestrel Realty — Business Card</title>
<link rel="stylesheet" href="https://fonts.googleapis.com/css2?family=Cinzel:wght@400;500&display=swap">
<style>
  :root {
    --backdrop: #e9ebee;
    --blue-deep: #1566d6;
    --blue-mid: #2a86ea;
    --blue-light: #4fa8f3;
    --card-white: #ffffff;
    --card-fog: #eceef1;
    --ink-grey: #5f6266;
    --mark-blue: #2f86e4;
    --rule: rgba(255, 255, 255, 0.55);
  }
  * { box-sizing: border-box; margin: 0; padding: 0; }
  html, body {
    width: 1200px;
    height: 1200px;
    overflow: hidden;
    background: var(--backdrop);
  }
  .canvas {
    position: relative;
    width: 1200px;
    height: 1200px;
  }
  .card {
    position: absolute;
    left: 180px;
    width: 840px;
    height: 480px;
    overflow: hidden;
    box-shadow: 0 14px 34px rgba(0, 0, 0, 0.18);
  }
  /* Back of card: name and contact */
  .card--back {
    top: 90px;
    background: linear-gradient(160deg, var(--blue-deep) 0%, var(--blue-mid) 55%, var(--blue-light) 100%);
    color: #fff;
    font-family: "Cinzel", serif;
  }
  .card__divider {
    position: absolute;
    left: 392px;
    top: 0;
    height: 100%;
    border-left: 2px dashed var(--rule);
  }
  .card__name {
    position: absolute;
    left: 80px;
    top: 208px;
    font-size: 36px;
    font-weight: 400;
    letter-spacing: 1px;
    font-variant: small-caps;
  }
  .card__contact {
    position: absolute;
    left: 440px;
    top: 92px;
    font-size: 21px;
    line-height: 1.25;
    font-variant: small-caps;
    list-style: none;
  }
  .card__contact .gap { margin-top: 28px; }
  .card__swoosh {
    position: absolute;
    left: 0;
    bottom: 0;
    width: 840px;
    height: 480px;
  }
  /* Front of card: company name */
  .card--front {
    top: 630px;
    background: radial-gradient(ellipse at 40% 35%, var(--card-white) 0%, var(--card-white) 45%, var(--card-fog) 100%);
  }
  .brand {
    position: absolute;
    left: 160px;
    top: 150px;
    display: flex;
    align-items: center;
    gap: 34px;
  }
  .brand__dot {
    width: 150px;
    height: 150px;
    border-radius: 50%;
    background: var(--mark-blue);
  }
  .brand__name {
    font-family: "Cinzel", serif;
    font-weight: 500;
    color: var(--ink-grey);
    line-height: 0.95;
  }
  .brand__name .line-1 { display: block; font-size: 84px; }
  .brand__name .line-2 { display: block; font-size: 46px; letter-spacing: 2px; }
  .card__edge {
    position: absolute;
    right: 0;
    bottom: 0;
    width: 840px;
    height: 480px;
  }
</style>
</head>
<body>
<main class="canvas">
  <section class="card card--back" aria-label="Business card back">
    <div class="card__divider"></div>
    <p class="card__name">Daniel Hale</p>
    <ul class="card__contact">
      <li>(01) 5550 4127</li>
      <li>daniel@kestrelrealty.com</li>
      <li class="gap">48 Harlow Street,</li>
      <li>Chicago,</li>
      <li>USA</li>
    </ul>
    <svg class="card__swoosh" viewBox="0 0 840 480" aria-hidden="true">
      <path d="M0 400 Q 220 450 420 480 L 0 480 Z" fill="#ffffff"/>
      <path d="M0 380 Q 200 430 380 480 L 420 480 Q 220 450 0 400 Z" fill="#ffffff" opacity="0.35"/>
    </svg>
  </section>

  <section class="card card--front" aria-label="Business card front">
    <div class="brand">
      <span class="brand__dot" aria-hidden="true"></span>
      <p class="brand__name"><span class="line-1">Kestrel</span><span class="line-2">Realty</span></p>
    </div>
    <svg class="card__edge" viewBox="0 0 840 480" aria-hidden="true">
      <defs>
        <linearGradient id="edgeBlue" x1="0" y1="0" x2="1" y2="0">
          <stop offset="0" stop-color="#4fa8f3"/>
          <stop offset="1" stop-color="#1566d6"/>
        </linearGradient>
      </defs>
      <path d="M560 480 Q 720 452 840 436 L 840 480 Z" fill="url(#edgeBlue)"/>
    </svg>
  </section>
</main>
</body>
</html>
```